Bodywork Quietude Business Card Design

I want to create a very elegant and sophisticated two sided business card for my massage practice (www.bodyworkquietude.net). I have attached the logo and a PDF with some ideas down for the back of the card but I am open to suggestions. I will want to tie in a post card and flyer to the card later.
Similar colors to website would be great.
Target Market(s)
High end clientele, people looking for a sophisticated spa experience.
Industry/Entity Type
Massage
Contact Information for Business Card
Bodywork Quietude
7318 Larkspur Ave S, Suite 305
Seattle, WA 98103
(206) 555-0147
www.bodyworkquietude.net
Look and feel

```html
<!DOCTYPE html>
<html lang="en">
<head>
<meta charset="utf-8">
<title>Bodywork Quietude – Business Card</title>
<link rel="stylesheet" href="https://fonts.googleapis.com/css2?family=Cinzel:wght@400;500&family=Lora:ital,wght@1,700&family=Source+Sans+3:wght@400&display=swap">
<style>
  :root {
    --stage: #181818;
    --card-light: #f2f2f2;
    --card-dark: #1b3140;
    --ink: #1b3140;
    --ink-soft: #222a30;
    --rule: #8e9ba5;
    --paper: #ffffff;
    --silver: #c9ccd0;
  }
  * { margin: 0; padding: 0; box-sizing: border-box; }
  html, body {
    width: 1200px; height: 900px; overflow: hidden;
    background: var(--stage);
  }
  .stage { position: relative; width: 1200px; height: 900px; }
  .card {
    position: absolute; top: 170px; width: 347px; height: 561px;
    text-align: center;
  }
  .card--front { left: 259px; background: var(--card-light); color: var(--ink-soft); }
  .card--back { left: 631px; background: var(--card-dark); color: var(--paper); }

  .brand { position: absolute; left: 0; right: 0; top: 72px; }
  .brand__mark {
    width: 40px; height: 40px; border-radius: 50%;
    margin: 0 auto 22px;
  }
  .card--front .brand__mark { background: var(--ink); }
  .card--back .brand__mark { background: var(--paper); }
  .brand__name {
    font-family: "Cinzel", serif; font-weight: 400;
    font-size: 22px; letter-spacing: 0.5px; line-height: 1;
  }
  .card--front .brand__name { color: var(--ink); }

  .contact { position: absolute; left: 0; right: 0; top: 322px; }
  .contact__name {
    font-family: "Cinzel", serif; font-weight: 500;
    font-size: 20px; letter-spacing: 0.5px; color: var(--ink); line-height: 24px;
  }
  .contact__role, .contact__line {
    font-family: "Source Sans 3", sans-serif; font-size: 14.5px; line-height: 20px;
  }
  .rule { width: 145px; height: 1px; background: var(--rule); margin: 12px auto 10px; }
  .contact__company {
    font-family: "Cinzel", serif; font-weight: 500;
    font-size: 16.5px; letter-spacing: 0.5px; color: var(--ink); line-height: 22px; margin-top: 4px;
  }

  .pitch {
    position: absolute; left: 0; right: 0; top: 314px;
    font-family: "Lora", serif; font-style: italic; font-weight: 700;
    font-size: 17.5px; line-height: 21.5px;
  }
  .ornament {
    position: absolute; left: 88px; top: 402px; width: 176px; height: 20px;
    border-radius: 10px;
    background: linear-gradient(90deg, rgba(201,204,208,0.15), rgba(201,204,208,0.55), rgba(201,204,208,0.15));
  }
  .services { top: 455px; }
</style>
</head>
<body>
<main class="stage">
  <section class="card card--front" aria-label="Business card front">
    <div class="brand">
      <div class="brand__mark"></div>
      <p class="brand__name">BODYWORK QUIETUDE</p>
    </div>
    <div class="contact">
      <p class="contact__name">DANIEL HARTLEY</p>
      <p class="contact__role">Managing Director</p>
      <div class="rule"></div>
      <p class="contact__line">(206) 555-0147</p>
      <p class="contact__line">www.bodyworkquietude.net</p>
      <div class="rule"></div>
      <p class="contact__company">BODYWORK QUIETUDE</p>
      <p class="contact__line">7318 Larkspur Ave S, Suite 305</p>
      <p class="contact__line">Seattle, WA 98103</p>
    </div>
  </section>

  <section class="card card--back" aria-label="Business card back">
    <div class="brand">
      <div class="brand__mark"></div>
      <p class="brand__name">BODYWORK QUIETUDE</p>
    </div>
    <p class="pitch">Experience the Most Unique,<br>Relaxing and Invitingly Deep<br>Massage of Your Life.....</p>
    <div class="ornament" role="img" aria-label="Silver decorative flourish divider"></div>
    <p class="pitch services">Ultra Relaxation<br>Nurturing Touch<br>Thai Yoga Massage</p>
  </section>
</main>
</body>
</html>
```